Business Card Design Project

I want a cleaner business card and envelope then what we have now, its too crowded.
Updates

I update with logo, this can be changed anyway you feel it looks best. I also have put gaurantee on there and extended time, this is my first time doing this. Also gave an example of current card

Target Market(s)

a wide array of customers from vantage 400 to small companies and cleints

Industry/Entity Type

Business

Requirements
Must have
• Need to have address, telephone number email
Nice to have
• a sharp professional card that stands out but is still very clean.
Should not have
• Not crazy looking

```html
<!DOCTYPE html>
<html lang="en">
<head>
<meta charset="utf-8">
<title>Halvor Insurance Group – Business Card, Front and Back</title>
<link rel="stylesheet" href="https://fonts.googleapis.com/css2?family=Arimo:wght@400&display=swap">
<style>
  :root {
    --page-bg: #3c3c3c;
    --card-white: #ffffff;
    --band-grey: #6b6b6b;
    --back-grey: #7a7a7a;
    --ink: #111111;
    --ink-soft: #555555;
    --band-text: #f2f2f2;
    --silver-light: #ececec;
    --silver-dark: #bdbdbd;
    --mark-ink: #1a1a1a;
  }
  * { box-sizing: border-box; margin: 0; padding: 0; }
  html, body {
    width: 1132px; height: 1200px; overflow: hidden;
    background: var(--page-bg);
    font-family: "Arimo", Arial, sans-serif;
  }
  .sheet {
    position: relative; width: 1132px; height: 1200px;
  }
  .card {
    position: absolute; left: 146px; width: 840px; height: 480px;
    box-shadow: 0 14px 30px rgba(0,0,0,.45);
    overflow: hidden;
  }

  /* Front */
  .card--front { top: 70px; background: var(--card-white); }
  .front__name {
    position: absolute; left: 44px; top: 58px;
    font-size: 44px; color: var(--ink); letter-spacing: .2px;
  }
  .front__title {
    position: absolute; left: 104px; top: 114px;
    font-size: 25px; color: var(--ink-soft);
  }
  .front__contact {
    position: absolute; left: 42px; top: 222px;
    list-style: none; font-size: 24px; line-height: 32px; color: var(--ink);
  }
  .front__contact .label { color: var(--ink-soft); }
  .front__emblem {
    position: absolute; right: 36px; top: 44px;
    width: 300px; height: 300px;
    background: linear-gradient(135deg, var(--silver-light), var(--silver-dark));
    box-shadow: 0 4px 10px rgba(0,0,0,.25);
  }
  .front__band {
    position: absolute; left: 0; bottom: 0; width: 100%; height: 96px;
    background: var(--band-grey);
  }
  .front__address {
    position: absolute; left: 20px; top: 16px;
    font-size: 15px; line-height: 20px; color: var(--band-text);
  }
  .front__brand {
    position: absolute; right: 24px; top: 18px;
    display: flex; align-items: center; gap: 8px;
  }
  .front__brand-square {
    width: 34px; height: 34px;
    background: linear-gradient(135deg, var(--silver-light), var(--silver-dark));
  }
  .front__brand-name {
    font-size: 15px; line-height: 17px; color: var(--band-text);
    letter-spacing: 1.5px; text-align: center;
  }

  /* Back */
  .card--back { top: 640px; background: var(--back-grey); }
  .back__strip-top {
    position: absolute; left: 0; top: 0; width: 100%; height: 18px;
    background: var(--card-white);
  }
  .back__strip-bottom {
    position: absolute; left: 0; bottom: 0; width: 100%; height: 52px;
    background: var(--card-white);
    border-top: 10px solid var(--back-grey);
  }
  .back__square {
    position: absolute; left: 340px; top: 52px;
    width: 160px; height: 160px;
    background: linear-gradient(135deg, var(--silver-light), var(--silver-dark));
    box-shadow: 0 6px 14px rgba(0,0,0,.35);
  }
  .back__wordmark {
    position: absolute; left: 0; top: 236px; width: 100%;
    text-align: center; color: var(--mark-ink);
  }
  .back__wordmark-name {
    display: block; font-size: 78px; letter-spacing: 14px; line-height: 84px;
  }
  .back__wordmark-sub {
    display: block; font-size: 36px; letter-spacing: 9px; line-height: 44px;
  }
</style>
</head>
<body>
<main class="sheet">
  <section class="card card--front" aria-label="Business card front">
    <h1 class="front__name">Nora Whitfield-Lane</h1>
    <p class="front__title">Operations Manager</p>
    <ul class="front__contact">
      <li><span class="label">Phone:</span> 555-214-3300 ext 118</li>
      <li><span class="label">Direct:</span> 555-214-0192</li>
      <li><span class="label">Fax:</span> 555-214-3305</li>
      <li>nwhitfield-lane@halvorinsure.com</li>
    </ul>
    <div class="front__emblem" aria-hidden="true"></div>
    <div class="front__band">
      <address class="front__address" style="font-style:normal">
        1870 Alder Crest Ave.<br>
        Maple Ridge, OH 45002<br>
        www.halvorinsure.com
      </address>
      <div class="front__brand">
        <span class="front__brand-square" aria-hidden="true"></span>
        <span class="front__brand-name">HALVOR<br>INSURANCE GROUP</span>
      </div>
    </div>
  </section>

  <section class="card card--back" aria-label="Business card back">
    <div class="back__strip-top"></div>
    <div class="back__square" aria-hidden="true"></div>
    <p class="back__wordmark">
      <span class="back__wordmark-name">HALVOR</span>
      <span class="back__wordmark-sub">INSURANCE GROUP</span>
    </p>
    <div class="back__strip-bottom"></div>
  </section>
</main>
</body>
</html>
```